依頼詳細
川辺ふれあい会の第7号の会報の原稿を依頼する。この活動を行うボランティア募集案内で①福祉車両、買い物、病院送迎ボランティア募集 ②子ども食堂開催の際のボランティア募集 ③夏季の子ども学習指導、ゲームや遊びボランティア募集 ④高齢者居場所づくりのサロンの話し相手のボランティア募集 ⑤生活支援の一般ボランティア募集(くさとり、清掃、片付けなど)のボランテイア募集の会報の編集依頼

記載項目
デザインを見てから、説明文は後日指示します。
サイズ
A4
ページ数
片面
希望イメージ
シンプル 複雑
単色 カラフル
暗い 明るい
日常 高級
遊び心 厳粛
未来的 伝統的
女性的 男性的
希望する色
青系
納品ファイル
• 高解像度JPG (.jpg)
補足説明
データをいただき、説明文の追加等を加筆し原稿をPDFにして印刷業者へ依頼する。

```html
<!DOCTYPE html>
<html lang="ja">
<head>
<meta charset="utf-8">
<title>川辺ふれあい会 会報第7号 ボランティア募集</title>
<link rel="stylesheet" href="https://fonts.googleapis.com/css2?family=M+PLUS+Rounded+1c:wght@500;700;800;900&family=Zen+Maru+Gothic:wght@700;900&display=swap">
<style>
  :root{
    --bg-top:#dbe9f8;
    --bg-bottom:#8fb3e8;
    --title-red:#e0202e;
    --issue-blue:#1b3f9e;
    --ink:#222a3a;
    --banner-pink:#f7b6cf;
    --banner-pink-deep:#ee8fb3;
    --banner-text:#ffffff;
    --banner-edge:#2f5fc8;
    --ring-pink:#f27fa7;
    --label-orange:#f06a1a;
    --label-red:#e0202e;
    --label-green:#2e9a3e;
    --label-purple:#8a3fb8;
    --new-tag:#e63b6f;
    --blob-pink:#f9c9dc;
    --blob-yellow:#fbe9a6;
    --blob-mint:#cdeedd;
  }
  *{box-sizing:border-box;margin:0;padding:0}
  html,body{width:849px;height:1200px;overflow:hidden;background:#fff}
  .sheet{
    position:relative;width:849px;height:1200px;overflow:hidden;
    background:linear-gradient(180deg,var(--bg-top) 0%,var(--bg-bottom) 100%);
    font-family:"M PLUS Rounded 1c",sans-serif;color:var(--ink);
  }
  .masthead{position:absolute;left:0;top:0;width:100%;height:112px}
  .org-name{
    position:absolute;left:26px;top:10px;font-family:"Zen Maru Gothic",sans-serif;
    font-weight:900;font-size:50px;color:var(--title-red);letter-spacing:1px;white-space:nowrap;
  }
  .org-name small{font-size:36px}
  .issue{position:absolute;right:28px;top:12px;text-align:right;color:var(--issue-blue);font-weight:800}
  .issue .no{font-size:36px;display:block;line-height:1.1}
  .issue .date{font-size:18px}
  .publisher{
    position:absolute;left:236px;top:80px;font-size:16px;font-weight:700;color:var(--issue-blue);letter-spacing:1px;white-space:nowrap;
  }
  .banner{
    position:absolute;left:82px;top:124px;width:690px;height:84px;border-radius:42px;
    background:linear-gradient(180deg,var(--banner-pink) 0%,var(--banner-pink-deep) 100%);
    display:flex;align-items:center;justify-content:center;
    font-family:"Zen Maru Gothic",sans-serif;font-weight:900;font-size:62px;color:var(--banner-text);
    letter-spacing:6px;-webkit-text-stroke:3px var(--banner-edge);paint-order:stroke fill;
  }
  .intro{position:absolute;left:42px;top:226px;width:600px;font-size:16px;font-weight:700;line-height:1.55}
  .intro .lead{font-size:22px;font-weight:800;margin-bottom:4px}
  .intro .note{color:var(--title-red)}
  .blob{position:absolute;border-radius:50%}
  .photo{
    position:absolute;border-radius:50%;border:7px solid var(--ring-pink);
    box-shadow:0 4px 10px rgba(40,60,120,.2);
  }
  .label{
    position:absolute;font-weight:900;font-size:32px;line-height:1.1;text-align:center;white-space:nowrap;
    -webkit-text-stroke:6px #fff;paint-order:stroke fill;
  }
  .tag{
    display:inline-block;background:var(--new-tag);color:#fff;font-size:14px;
    border-radius:50%;width:40px;height:40px;line-height:40px;text-align:center;
    -webkit-text-stroke:0;vertical-align:middle;margin-right:4px;
  }
  .desc{position:absolute;font-size:14px;font-weight:700;line-height:1.6;white-space:nowrap}
  .footer{
    position:absolute;left:0;top:1116px;width:100%;height:84px;text-align:center;font-weight:900;
  }
  .footer .line1{font-size:28px;color:var(--issue-blue)}
  .footer .line1 em{font-style:normal;color:var(--title-red)}
  .footer .line2{font-size:26px;color:var(--title-red);margin-top:2px}
</style>
</head>
<body>
<div class="sheet">
  <header class="masthead">
    <h1 class="org-name"><small>NPO法人</small>川辺ふれあい会</h1>
    <div class="issue"><span class="no">会報第7号</span><span class="date">2022.2.1発行</span></div>
    <p class="publisher">発行責任者　理事長　山本和子　TEL 0123-45-6789</p>
  </header>

  <h2 class="banner">ボランティア募集</h2>

  <section class="intro">
    <p class="lead">川辺市にお住いの方へ</p>
    <p>ふれあいボランティアの活動をはじめてみませんか。2022年の事業計画において新規事業を計画しています。</p>
    <p>その事業を進めるための新たなボランティアを募集します。</p>
    <p>少しの時間でも大丈夫です。お気軽にご参加ください。</p>
    <p class="note">ボランティアを希望される方は後日詳しく説明を行います。</p>
  </section>

  <div class="blob" style="left:70px;top:500px;width:200px;height:170px;background:var(--blob-yellow)"></div>
  <div class="blob" style="left:600px;top:470px;width:230px;height:190px;background:var(--blob-pink)"></div>
  <div class="blob" style="left:290px;top:790px;width:230px;height:160px;background:var(--blob-mint)"></div>
  <div class="blob" style="left:40px;top:960px;width:220px;height:150px;background:var(--blob-pink)"></div>
  <div class="blob" style="left:590px;top:950px;width:230px;height:150px;background:var(--blob-yellow)"></div>

  <div class="photo" role="img" aria-label="車椅子の方を送迎するボランティアの写真" style="left:100px;top:488px;width:180px;height:180px;background:linear-gradient(135deg,#dfe8f0,#a9bccf)"></div>
  <div class="label" style="left:60px;top:410px;width:260px;color:var(--label-orange)">送迎<br>ボランティア</div>

  <div class="photo" role="img" aria-label="子ども食堂で食事をする子どもたちの写真" style="left:575px;top:480px;width:180px;height:180px;background:linear-gradient(135deg,#f4dcc4,#d9a982)"></div>
  <div class="label" style="left:520px;top:408px;width:300px;color:var(--label-red)"><span class="tag">新規</span>こども食堂<br>ボランティア</div>

  <p class="desc" style="left:296px;top:500px">一番利用者が多いのが<br>送迎ボランティアです。<br>福祉車両の運転に協力いただける方<br>を募集しています。</p>

  <p class="desc" style="left:296px;top:612px">地域の子育て中の親子に<br>月1回食事を提供します。<br>お手伝いできる方募集中です。</p>

  <div class="photo" role="img" aria-label="庭の草取りなど日常支援の様子の写真" style="left:320px;top:760px;width:180px;height:180px;background:linear-gradient(135deg,#d8e9c9,#94b87c)"></div>
  <div class="label" style="left:280px;top:690px;width:260px;color:var(--label-green)">日常支援<br>ボランティア</div>

  <p class="desc" style="left:570px;top:800px">日常生活で困っている<br>草取り、清掃、片付けなどを<br>お手伝いするボランティアです。</p>

  <div class="photo" role="img" aria-label="学習する子どもの写真" style="left:70px;top:935px;width:170px;height:170px;background:linear-gradient(135deg,#e7e1f2,#b5a6d6)"></div>
  <div class="label" style="left:30px;top:862px;width:250px;color:var(--label-purple)">学習<br>ボランティア</div>

  <p class="desc" style="left:290px;top:950px">夏休み期間中の学習支援と<br>ゲームや遊びの場を楽しく<br>運営するボランティアです。</p>

  <div class="photo" role="img" aria-label="高齢者サロンで話す人々の写真" style="left:600px;top:935px;width:170px;height:170px;background:linear-gradient(135deg,#f2e4d8,#cfa98f)"></div>
  <div class="label" style="left:545px;top:862px;width:280px;color:var(--label-red)"><span class="tag">新規</span>サロン<br>ボランティア</div>

  <p class="desc" style="left:340px;top:1050px">高齢者の居場所づくりとして<br>毎月1回楽しい会を開きます。</p>

  <footer class="footer">
    <p class="line1">会員、ボランティア、家庭菜園希望者 <em>随時募集中</em></p>
    <p class="line2">お問い合わせは事務局まで</p>
  </footer>
</div>
</body>
</html>
```